Re-Design the flow of the Orvane Framework

The orvane framework is a 10 step model that helps teams/organizations become high performing. Attached the model which i created. I love the design as it is but i used a template i don't owe the rights of so i would like to use this platform to see what you can come up with the redesign this flow while keeping the key elements in place. I like the flow, i like the cleanness and i like it to be compact.

Target Market(s)

Organizational change / Leadership/ Consultancy

Industry/Entity Type

Leadership

Requirements
Must have
• Keep as much as possible the flow and feel of the attached
Nice to have
• -Maybe some twist in how the different parts connect (not a must)
Should not have
• Less or more steps than added in the attached file

```html
<!DOCTYPE html>
<html lang="en">
<head>
<meta charset="utf-8">
<title>Orvane Framework</title>
<link rel="stylesheet" href="https://fonts.googleapis.com/css2?family=Heebo:wght@400;500;800&display=swap">
<style>
  :root {
    --purple: #472c7d;
    --red: #de2607;
    --orange: #f5a623;
    --white: #ffffff;
  }
  html, body {
    margin: 0;
    padding: 0;
    width: 1200px;
    height: 998px;
    overflow: hidden;
    background: var(--white);
  }
  .framework {
    display: block;
    width: 1200px;
    height: 998px;
    font-family: "Heebo", sans-serif;
  }
  .segment { stroke: var(--white); stroke-width: 12; stroke-linejoin: miter; }
  .fill-purple { fill: var(--purple); }
  .fill-red { fill: var(--red); }
  .fill-orange { fill: var(--orange); }
  .step-label { fill: var(--white); font-size: 23px; font-weight: 400; text-anchor: middle; }
  .hub-label { fill: var(--white); font-size: 40px; font-weight: 500; text-anchor: middle; }
  .loop-label { fill: var(--white); font-size: 27px; font-weight: 500; }
  .bullet-label { fill: var(--white); font-size: 20px; }
  .arc-title { font-size: 96px; font-weight: 800; }
  .arc-title-purple { fill: var(--purple); }
  .arc-title-red { fill: var(--red); }
  .icon-line { fill: none; stroke: var(--white); stroke-width: 6; stroke-linecap: round; stroke-linejoin: round; }
  .icon-solid { fill: var(--white); }
  .pulse-purple { fill: none; stroke: var(--purple); stroke-width: 4; stroke-linejoin: round; }
  .pulse-red { fill: none; stroke: var(--red); stroke-width: 4; stroke-linejoin: round; }
  .icon-slot { fill: var(--white); opacity: 0.92; }
</style>
</head>
<body>
<svg class="framework" viewBox="0 0 1920 1597" xmlns="http://www.w3.org/2000/svg">
  <defs>
    <path id="arc-human" d="M198.1,462.4 A490,490 0 0 1 1045,600"/>
    <path id="arc-self" d="M37,690 A555,555 0 0 0 560,1342"/>
    <path id="arc-unleash" d="M823,1059.5 A545,545 0 0 0 1821.4,928.1"/>
  </defs>

  <!-- Foundation ring -->
  <g class="ring ring-foundation">
    <path class="segment fill-red" d="M120,787 A465,465 0 0 1 256.2,458.2 L417.4,619.4 A237,237 0 0 0 348,787 Z"/>
    <path class="segment fill-orange" d="M256.2,458.2 A465,465 0 0 1 585,322 L585,550 A237,237 0 0 0 417.4,619.4 Z"/>
    <path class="segment fill-purple" d="M585,322 A465,465 0 0 1 913.8,458.2 L752.6,619.4 A237,237 0 0 0 585,550 Z"/>
    <path class="segment fill-red" d="M913.8,458.2 A465,465 0 0 1 1050,787 L822,787 A237,237 0 0 0 752.6,619.4 Z"/>
    <path class="segment fill-purple" d="M256.2,1115.8 A465,465 0 0 1 120,787 L348,787 A237,237 0 0 0 417.4,954.6 Z"/>
    <path class="segment fill-orange" d="M665.7,1245 A465,465 0 0 1 256.2,1115.8 L417.4,954.6 A237,237 0 0 0 626.2,1020.4 Z"/>
  </g>

  <!-- Excellence ring -->
  <g class="ring ring-excellence">
    <path class="segment fill-red" d="M1753,787 A458,458 0 0 1 1618.9,1110.9 L1468.2,960.2 A245,245 0 0 0 1540,787 Z"/>
    <path class="segment fill-purple" d="M1618.9,1110.9 A458,458 0 0 1 1295,1245 L1295,1032 A245,245 0 0 0 1468.2,960.2 Z"/>
    <path class="segment fill-red" d="M1295,1245 A458,458 0 0 1 971.1,1110.9 L1121.8,960.2 A245,245 0 0 0 1295,1032 Z"/>
    <path class="segment fill-orange" d="M1527,787 L1527,557 L1473,557 L1640,330 L1808,557 L1753,557 L1753,787 Z"/>
  </g>

  <!-- Crossing and loop arrows -->
  <g class="crossing">
    <path class="segment fill-purple" d="M1059.5,719.5 A480,480 0 0 0 960,470 A458,458 0 0 1 1153.5,351.4 L1211.2,556.8 A245,245 0 0 0 1059.5,719.5 Z"/>
    <path class="segment fill-purple" d="M1200,330 L1625,330 L1460,550 L1290,550 L1290,578 L1040,515 L1190,305 Z"/>
    <path class="segment fill-orange" d="M822,787 L1050,787 A245,245 0 0 0 1107.3,944.5 L960,1104 L913.8,1115.8 L813.9,848.3 A237,237 0 0 0 822,787 Z"/>
    <path class="segment fill-purple" d="M913.8,1115.8 A465,465 0 0 1 728.7,1229.2 L736.4,1253 L490.7,1165.4 L651.4,991.5 L658.2,1012.4 A237,237 0 0 0 813.9,848.3 Z"/>
  </g>

  <!-- Hubs -->
  <g class="hub hub-foundation">
    <circle cx="585" cy="787" r="158" class="fill-purple"/>
    <g class="fill-purple">
      <polygon points="510,580 545,622 510,632"/>
      <polygon points="682,586 680,642 642,628"/>
      <polygon points="740,714 800,714 752,752"/>
      <polygon points="382,694 436,700 420,738"/>
      <polygon points="372,866 418,828 434,866"/>
      <polygon points="490,994 496,934 534,950"/>
    </g>
    <text class="hub-label" x="585" y="753">Capabilities</text>
    <text class="hub-label" x="585" y="803">Driving a Solid</text>
    <text class="hub-label" x="585" y="853">Foundation</text>
  </g>
  <g class="hub hub-excellence">
    <circle cx="1295" cy="787" r="158" class="fill-red"/>
    <g class="fill-red">
      <polygon points="1080,860 1130,820 1140,858"/>
      <polygon points="1460,838 1498,880 1444,876"/>
      <polygon points="1196,988 1200,930 1238,946"/>
      <polygon points="1370,998 1334,956 1370,940"/>
    </g>
    <text class="hub-label" x="1293" y="758">Capabilities</text>
    <text class="hub-label" x="1293" y="808">Maximizing</text>
    <text class="hub-label" x="1293" y="858">Excellence</text>
  </g>

  <!-- Step labels and icons -->
  <g class="step step-strategy">
    <text class="step-label" x="274" y="594">Develop a</text>
    <text class="step-label" x="274" y="620">Master plan</text>
    <text class="step-label" x="274" y="646">(strategy)</text>
    <g transform="translate(273,710)">
      <circle r="32" class="icon-line"/>
      <circle r="18" class="icon-line"/>
      <circle r="6" class="icon-solid"/>
      <path class="icon-line" d="M0,-44 V-24 M0,24 V44 M-44,0 H-24 M24,0 H44"/>
    </g>
  </g>

  <g class="step step-safety">
    <text class="step-label" x="469" y="407">Cultivate</text>
    <text class="step-label" x="469" y="433">Psychological</text>
    <text class="step-label" x="469" y="459">Safety &amp; Ownership</text>
    <rect class="icon-slot" x="414" y="480" width="70" height="66" rx="8" role="img" aria-label="Group of people icon"/>
  </g>

  <g class="step step-purpose-passion">
    <text class="step-label" x="711" y="408">Tap into peoples</text>
    <text class="step-label" x="711" y="434">Purpose and Passion</text>
    <text class="step-label" x="711" y="460">(intrinsic motivation)</text>
    <g transform="translate(715,518) scale(1.15)">
      <path class="icon-solid" d="M0,30 C-42,2 -38,-30 -18,-32 C-8,-33 0,-25 0,-17 C0,-25 8,-33 18,-32 C38,-30 42,2 0,30 Z"/>
      <polyline class="pulse-purple" points="-24,-2 -11,-2 -6,-13 1,10 6,-5 11,-2 24,-2"/>
    </g>
  </g>

  <g class="step step-growth">
    <text class="step-label" x="910" y="588">Unlock culture</text>
    <text class="step-label" x="910" y="614">of personal</text>
    <text class="step-label" x="910" y="640">growth &amp;</text>
    <text class="step-label" x="910" y="666">development</text>
    <rect class="icon-slot" x="876" y="692" width="84" height="70" rx="8" role="img" aria-label="People with rising growth arrow icon"/>
  </g>

  <g class="step step-feedback">
    <rect class="icon-slot" x="928" y="820" width="74" height="88" rx="30" role="img" aria-label="Head with gears icon"/>
    <text class="step-label" x="963" y="947">Prioritize</text>
    <text class="step-label" x="963" y="973">Feedback &amp;</text>
    <text class="step-label" x="963" y="999">Transparency</text>
  </g>

  <g class="step step-vision">
    <rect class="icon-slot" x="230" y="830" width="70" height="68" rx="8" role="img" aria-label="Telescope icon"/>
    <text class="step-label" x="255" y="937">Identify</text>
    <text class="step-label" x="255" y="963">Purpose</text>
    <text class="step-label" x="255" y="989">Activators</text>
    <text class="step-label" x="255" y="1015">(Vision)</text>
  </g>

  <g class="step step-why">
    <g transform="translate(427,1045) scale(1.15)">
      <path class="icon-solid" d="M0,30 C-42,2 -38,-30 -18,-32 C-8,-33 0,-25 0,-17 C0,-25 8,-33 18,-32 C38,-30 42,2 0,30 Z"/>
      <polyline class="pulse-red" points="-24,-2 -11,-2 -6,-13 1,10 6,-5 11,-2 24,-2" style="stroke: var(--orange)"/>
    </g>
    <text class="step-label" x="408" y="1111">Discover your</text>
    <text class="step-label" x="408" y="1137">purpose. Why</text>
    <text class="step-label" x="408" y="1163">Do you exist?</text>
  </g>

  <g class="step step-community">
    <rect class="icon-slot" x="1112" y="1032" width="96" height="88" rx="44" role="img" aria-label="Hands joined in a circle icon"/>
    <text class="step-label" x="1248" y="1150" style="text-anchor:end">Empower the</text>
    <text class="step-label" x="1248" y="1176" style="text-anchor:end">community from</text>
    <text class="step-label" x="1248" y="1202" style="text-anchor:end">bottom-up</text>
  </g>

  <g class="step step-spotlight">
    <g transform="translate(1410,1075)">
      <path class="icon-solid" d="M-26,-36 H26 V-6 C26,12 14,22 0,22 C-14,22 -26,12 -26,-6 Z"/>
      <path class="icon-line" d="M-26,-28 H-36 V-14 C-36,-4 -28,2 -22,2 M26,-28 H36 V-14 C36,-4 28,2 22,2"/>
      <rect class="icon-solid" x="-5" y="20" width="10" height="14"/>
      <rect class="icon-solid" x="-20" y="32" width="40" height="8"/>
    </g>
    <text class="step-label" x="1316" y="1150" style="text-anchor:start">Put excellent (team)</text>
    <text class="step-label" x="1316" y="1176" style="text-anchor:start">performance in</text>
    <text class="step-label" x="1316" y="1202" style="text-anchor:start">the spotlight</text>
  </g>

  <g class="step step-monitor">
    <g transform="translate(1584,862)">
      <circle r="28" class="icon-line" style="stroke-width:7"/>
      <path class="icon-line" d="M21,21 L50,42" style="stroke-width:11"/>
      <polyline class="icon-line" style="stroke-width:4" points="-20,2 -9,2 -4,-12 3,12 8,-3 20,-3"/>
    </g>
    <text class="step-label" x="1599" y="941">Monitor</text>
    <text class="step-label" x="1599" y="967">engagement</text>
    <text class="step-label" x="1599" y="993">Real-time</text>
  </g>

  <g class="step step-potential">
    <text class="step-label" x="1642" y="484">Reaching Full</text>
    <text class="step-label" x="1642" y="510">Potential Of</text>
    <text class="step-label" x="1642" y="536">People &amp; Organization</text>
    <g class="outcome-list">
      <circle class="icon-solid" cx="1548" cy="572" r="6"/>
      <text class="bullet-label" x="1562" y="579">Productivity upto</text>
      <text class="bullet-label" x="1562" y="604">800%</text>
      <circle class="icon-solid" cx="1548" cy="624" r="6"/>
      <text class="bullet-label" x="1562" y="631">Employee</text>
      <text class="bullet-label" x="1562" y="656">engagement &gt;90%</text>
      <circle class="icon-solid" cx="1548" cy="675" r="6"/>
      <text class="bullet-label" x="1562" y="682">Max discretionary</text>
      <text class="bullet-label" x="1562" y="707">effort gap</text>
      <circle class="icon-solid" cx="1548" cy="726" r="6"/>
      <text class="bullet-label" x="1562" y="733">High resilience to</text>
      <text class="bullet-label" x="1562" y="758">change</text>
    </g>
  </g>

  <!-- Loop labels -->
  <g class="loop-labels">
    <text class="loop-label" x="598" y="1107">(RE)START HERE</text>
    <text class="loop-label" x="615" y="1153">(RE)INVENT HERE</text>
    <text class="loop-label" x="1199" y="424">(RE)START HERE</text>
    <text class="loop-label" x="1216" y="470">(RE)INVENT HERE</text>
  </g>

  <!-- Arc titles -->
  <text class="arc-title arc-title-purple"><textPath href="#arc-human" startOffset="60">Human Experience</textPath></text>
  <text class="arc-title arc-title-purple"><textPath href="#arc-self" startOffset="250">Self Direction</textPath></text>
  <text class="arc-title arc-title-red"><textPath href="#arc-unleash" startOffset="190">Unleash Engangement</textPath></text>
</svg>
</body>
</html>
```